Website design for Cloud Scheduling Company

We have a design build that is based on a corporate template. the structure and content is there but the design does not match the 'feel' of what we are going for from a design perspective.
http://plumvexo.com/demo/fen/

please follow this structure for the site layout but add new ideas also.

Scheduling is boring and typically a serious topic, with our new logo we are looking to bring a quirky, fun feeling to what our site does.

It is a powerful scheduling platform that is used mainly in Volunteer environments and we want our brand to reflect this.

A lot of sites use images of real people in photographs but i would like to see us use more vector graphics and illustrations in the design so it is a bit more exciting.

The homepage should have a large screen capture of the app on different devices (large monitor, tablet, and smartphone) which is pretty standard for this type of website.i have attached a jpeg where you can get images from as well as the logo so you can get a sense of the look and feel.

this is what I envision being the image in the main banner as it showcases the application https://www.trindlesk.ca/search?q=responsive&biw=1920&bih=920&source=lnms&tbm=isch&sa=X&ved=0ahUKEwiAlqahjv_KAhXrlIMKHToqB5oQ_AUIBigB#imgrc=a75LOlLuwcKyqM%3A

Again, what I need for this project is a design for the site at http://plumvexo.com/demo/fen/. it is already coded but i need a netter design. focus on homepage, pricing page and a general subpage please.

Target Market(s)

Volunteer organization Administrators

Industry/Entity Type

It Company

Number of Pages Required

3 page

Font styles to use
Sans Serif

Colors
0355a3
f37122

Requirements
Nice to have
• use graphics instead of photographs. you can include some photos but i want the look and feel to be consistent with the playfulness of the logo so the site isnt too serious. The site still has to be professional.

```html
<!DOCTYPE html>
<html lang="en">
<head>
<meta charset="utf-8">
<title>Fenplanner — Pricing</title>
<link rel="stylesheet" href="https://fonts.googleapis.com/css2?family=Arimo:wght@400;700&family=Open+Sans:wght@400;600;700&display=swap">
<style>
:root{
  --blue:#0355a3;
  --orange:#f37122;
  --orange-light:#f6925a;
  --dark:#403d3c;
  --panel:#f4f3f3;
  --row:#ffffff;
  --text:#555555;
  --footer:#1f232d;
  --footer-text:#8a8d94;
}
*{margin:0;padding:0;box-sizing:border-box}
html,body{width:1200px;height:942px;overflow:hidden;background:#fff;font-family:'Open Sans',sans-serif}
.page{position:relative;width:1200px;height:942px}
.site-header{position:absolute;top:0;left:0;width:1200px;height:79px;border-top:3px solid var(--blue);background:#fff}
.brand{position:absolute;left:220px;top:26px;display:flex;align-items:center;gap:7px;color:var(--blue);font-weight:700;font-size:24px;letter-spacing:-0.5px;white-space:nowrap}
.brand .dot{width:26px;height:26px;border-radius:50%;background:var(--orange)}
.main-nav{position:absolute;left:477px;top:36px;display:flex;align-items:center;font-size:10px;color:#333;text-transform:uppercase;white-space:nowrap}
.main-nav a{color:inherit;text-decoration:none;white-space:nowrap}
.main-nav a.active{color:var(--orange);font-weight:600}
.main-nav .sep{margin:0 15px;color:#333}
.contact-icons{position:absolute;left:928px;top:33px;display:flex;gap:7px}
.contact-icons svg{width:18px;height:18px}
.hero{position:absolute;top:79px;left:0;width:1200px;height:239px;background:linear-gradient(180deg,#4d6590,#475c83);text-align:center;color:#fff}
.hero h1{position:absolute;top:66px;width:100%;font-family:'Arimo',sans-serif;font-weight:400;font-size:48px;letter-spacing:0.5px}
.hero p{position:absolute;top:120px;width:100%;font-size:17.5px;line-height:20px;color:#eef1f6}
.humps{position:absolute;top:298px;left:0;width:1200px;height:22px}
.plans{position:absolute;top:318px;left:220px;width:760px;height:300px}
.plan{position:absolute;top:0;width:187px;height:300px;background:var(--panel);border-bottom:2px solid #e2e2e2;text-align:center;color:var(--text)}
.plan-head{position:absolute;top:8px;left:9px;width:169px;height:50px;background:var(--blue);color:#fff;font-family:'Arimo',sans-serif;font-weight:400;font-size:17px;padding-top:10px;text-transform:uppercase}
.price{position:absolute;top:42px;left:56px;width:76px;height:76px;border-radius:50%;background:#fff;box-shadow:0 2px 2px rgba(0,0,0,.18);font-family:'Arimo',sans-serif;font-weight:700;font-size:27px;color:#666;line-height:76px}
.features{position:absolute;top:127px;left:0;width:100%;list-style:none;font-size:12px}
.features li{height:26.5px;line-height:26.5px;white-space:nowrap}
.features li:nth-child(even){background:var(--row)}
.cta{position:absolute;top:248px;left:28px;width:130px;height:35px;background:var(--orange);color:#fff;font-weight:600;font-size:12px;line-height:35px;text-decoration:none}
.plan.featured{background:var(--orange);border-bottom-color:var(--orange);color:#fff}
.plan.featured .plan-head{background:var(--dark)}
.plan.featured .features li:nth-child(even){background:var(--orange-light)}
.plan.featured .cta{background:var(--dark)}
.site-footer{position:absolute;top:678px;left:0;width:1200px;height:264px;background:var(--footer);text-align:center}
.footer-nav{position:absolute;top:52px;left:0;width:100%;display:flex;justify-content:center;font-size:10px;color:var(--footer-text);text-transform:uppercase;letter-spacing:.3px;white-space:nowrap}
.footer-nav a{color:inherit;text-decoration:none}
.footer-nav a.active{color:#fff}
.footer-nav .sep{margin:0 16px}
.footer-brand{position:absolute;top:108px;left:0;width:100%;display:flex;justify-content:center;align-items:center;gap:8px;color:#5a5d63;font-weight:700;font-size:32px}
.footer-brand .dot{width:30px;height:30px;border-radius:50%;background:#5a5d63}
.social{position:absolute;top:858px;left:521px;display:flex;gap:6px}
.social{top:181px}
.social span{width:22px;height:22px;border-radius:50%;background:#5d6067}
.social span:first-child{background:#4664a8}
.copyright{position:absolute;top:215px;width:100%;font-size:10.5px;color:var(--footer-text)}
.copyright strong{color:#fff;font-weight:400}
</style>
</head>
<body>
<div class="page">
  <header class="site-header">
    <div class="brand"><span class="dot"></span>fenplanner.com</div>
    <nav class="main-nav">
      <a class="active" href="#">Home</a><span class="sep">|</span>
      <a href="#">About Us</a><span class="sep">|</span>
      <a href="#">Services</a><span class="sep">|</span>
      <a href="#">Projects</a><span class="sep">|</span>
      <a href="#">Blog</a><span class="sep">|</span>
      <a href="#">Contact Us</a>
    </nav>
    <div class="contact-icons">
      <svg viewBox="0 0 20 20" aria-label="Phone"><circle cx="10" cy="10" r="9" fill="none" stroke="#666" stroke-width="1.3"/><path d="M6.5 5.5l2 0.3 0.6 2-1.1 1c.6 1.3 1.5 2.2 2.7 2.8l1-1.1 2 .6.3 2c-4.4.6-8-3-7.5-7.6z" fill="none" stroke="#666" stroke-width="1.1"/></svg>
      <svg viewBox="0 0 20 20" aria-label="Email"><circle cx="10" cy="10" r="9" fill="none" stroke="#666" stroke-width="1.3"/><rect x="5" y="6.5" width="10" height="7" rx="1" fill="#666"/><path d="M5.5 7l4.5 3.5L14.5 7" fill="none" stroke="#fff" stroke-width="1"/></svg>
    </div>
  </header>

  <section class="hero">
    <h1>PRICING TABLE</h1>
    <p>Lorem ipsum dolor sit amet, consectetuer adipiscing elit,<br>sed diam nonummy nibh euismod tincidunt.</p>
  </section>

  <svg class="humps" viewBox="0 0 1200 22" aria-hidden="true">
    <g fill="var(--panel)">
      <path d="M244 22C280 22 282 4 314 4S348 22 384 22Z"/>
      <path d="M626 22C662 22 664 4 696 4S730 22 766 22Z"/>
      <path d="M816 22C852 22 854 4 886 4S920 22 956 22Z"/>
    </g>
    <path d="M432 22C468 22 470 4 502 4S536 22 572 22Z" fill="var(--orange)"/>
    <g fill="#9a9a9a">
      <path d="M309 13h10l-5 5z"/><path d="M691 13h10l-5 5z"/><path d="M881 13h10l-5 5z"/>
    </g>
    <path d="M497 13h10l-5 5z" fill="#fff"/>
  </svg>

  <section class="plans">
    <article class="plan" style="left:0">
      <h2 class="plan-head">Enterprise</h2>
      <div class="price">$59</div>
      <ul class="features"><li>Lorem ipsum dolor sit amet</li><li>Consectetur adipiscing elit</li><li>Nullam in feugiat turpis</li><li>Vestibulum posuere mauris</li></ul>
      <a class="cta" href="#">GET STARTED</a>
    </article>
    <article class="plan featured" style="left:190px">
      <h2 class="plan-head">Professional</h2>
      <div class="price">$29</div>
      <ul class="features"><li>Lorem ipsum dolor sit amet</li><li>Consectetur adipiscing elit</li><li>Nullam in feugiat turpis</li><li>Vestibulum posuere mauris</li></ul>
      <a class="cta" href="#">GET STARTED</a>
    </article>
    <article class="plan" style="left:382px">
      <h2 class="plan-head">Standard</h2>
      <div class="price">$17</div>
      <ul class="features"><li>Lorem ipsum dolor sit amet</li><li>Consectetur adipiscing elit</li><li>Nullam in feugiat turpis</li><li>Vestibulum posuere mauris</li></ul>
      <a class="cta" href="#">GET STARTED</a>
    </article>
    <article class="plan" style="left:573px">
      <h2 class="plan-head">Basic</h2>
      <div class="price">$9</div>
      <ul class="features"><li>Lorem ipsum dolor sit amet</li><li>Consectetur adipiscing elit</li><li>Nullam in feugiat turpis</li><li>Vestibulum posuere mauris</li></ul>
      <a class="cta" href="#">GET STARTED</a>
    </article>
  </section>

  <footer class="site-footer">
    <nav class="footer-nav">
      <a class="active" href="#">Home</a><span class="sep">|</span>
      <a href="#">About Us</a><span class="sep">|</span>
      <a href="#">Services</a><span class="sep">|</span>
      <a href="#">Projects</a><span class="sep">|</span>
      <a href="#">Blog</a><span class="sep">|</span>
      <a href="#">Contact Us</a>
    </nav>
    <div class="footer-brand"><span class="dot"></span>fenplanner.com</div>
    <div class="social" aria-label="Social links"><span></span><span></span><span></span><span></span><span></span><span></span></div>
    <p class="copyright">©2016 <strong>Fenplanner.</strong> All rights reserved.</p>
  </footer>
</div>
</body>
</html>
```